Ferris + Oakdale Architecture Ltd Stationary rebrand Lead designer to create a fresh clean modern...

We have recieved a great new logo design and now we are after a consistant fresh and modern stationary to match the new design. Business card design, Letter Head design, presentatnion folders and other stationery within the package. I have also added some of our existing layouts for presentation we would like updating with the new look, We would like a clean modern fresh design that looks visually pleasing on the page. we cant wait to see what you come up with!!!!

Target Market(s)

young professionals and middle age clients

Industry/Entity Type

Architect

Contact Information for Business Card

i have uploarded our orginal business card that has all the details attached.

Font styles to use
Sans Serif

Colors
000000
ffffff
d3d3d3

Requirements
Must have
• Logo and our contact information
Nice to have
• white sape around the card to give a clean look.

```html
<!DOCTYPE html>
<html lang="en">
<head>
<meta charset="utf-8">
<title>Ferris + Oakdale Architecture — Business Card</title>
<link href="https://fonts.googleapis.com/css2?family=Poppins:wght@300;400;500&display=swap" rel="stylesheet">
<style>
  :root {
    --backdrop: #262626;
    --card: #161616;
    --white: #ffffff;
    --silver: #d3d3d3;
    --muted: #8a8a8a;
    --rule: #5a5a5a;
  }
  * { margin: 0; padding: 0; box-sizing: border-box; }
  html, body {
    width: 1200px; height: 800px; overflow: hidden;
    background: var(--backdrop);
    font-family: "Poppins", sans-serif;
  }
  .stage {
    width: 1200px; height: 800px;
    display: flex; align-items: center; justify-content: center; gap: 60px;
  }
  .card {
    width: 520px; height: 298px;
    background: var(--card);
    position: relative;
    box-shadow: 0 10px 30px rgba(0,0,0,0.45);
  }
  /* Front */
  .card-front .brand {
    position: absolute; left: 0; right: 0; top: 104px;
    display: flex; align-items: center; justify-content: center; gap: 14px;
  }
  .brand-square {
    width: 22px; height: 22px; border: 3px solid var(--silver);
  }
  .card-front .brand-name {
    color: var(--silver); font-weight: 400; font-size: 24px; letter-spacing: 1px;
  }
  .card-front .web {
    position: absolute; left: 0; right: 0; bottom: 44px; text-align: center;
    color: var(--muted); font-size: 11px; font-weight: 300; letter-spacing: 4px;
  }
  /* Back */
  .card-back .identity {
    position: absolute; left: 0; top: 0; width: 270px; height: 100%;
    display: flex; flex-direction: column; align-items: center; justify-content: center; gap: 14px;
  }
  .identity .brand-square { width: 50px; height: 50px; border-width: 6px; border-color: var(--white); }
  .identity .brand-name {
    color: var(--white); font-weight: 400; text-align: center; line-height: 1.25;
    font-size: 15px; letter-spacing: 1.5px; text-transform: uppercase;
  }
  .identity .brand-name span { display: block; font-size: 11px; letter-spacing: 6px; }
  .divider {
    position: absolute; left: 270px; top: 40px; bottom: 40px; width: 1px;
    background: linear-gradient(var(--card), var(--rule) 20%, var(--rule) 80%, var(--card));
  }
  .details {
    position: absolute; left: 296px; top: 38px; color: var(--white);
  }
  .details .person { font-size: 17px; font-weight: 500; line-height: 1.1; }
  .details .role { font-size: 10px; font-weight: 400; margin-bottom: 12px; }
  .details p { font-size: 10px; font-weight: 300; line-height: 1.45; padding-left: 14px; }
  .details .gap { margin-bottom: 8px; }
</style>
</head>
<body>
<main class="stage">
  <section class="card card-front">
    <div class="brand">
      <div class="brand-square"></div>
      <div class="brand-name">Ferris + Oakdale</div>
    </div>
    <div class="web">www.foarchitecture.co.nz</div>
  </section>

  <section class="card card-back">
    <div class="identity">
      <div class="brand-square"></div>
      <div class="brand-name">Ferris + Oakdale<span>Architecture</span></div>
    </div>
    <div class="divider"></div>
    <div class="details">
      <div class="person">Daniel Ferris</div>
      <div class="role">Director</div>
      <p>62 Harlow Street</p>
      <p class="gap">Brackenridge 7700</p>
      <p class="gap">PO Box 4180, Brackenridge 7740</p>
      <p>P. 03 555 0148</p>
      <p>C. 0274 555 219</p>
      <p>daniel@foarchitecture.co.nz</p>
      <p>www.foarchitecture.co.nz</p>
    </div>
  </section>
</main>
</body>
</html>
```